VRB (Mirela Dovanski Wellness) Website supporting women to live a healthy lifestyle

Hi
I'm thrilled to be working together to bring a fresh look to my website! As an Integrative Health Practitioner, my mission is to support and empower women on their journey to reclaim their health and well-being. The website should feel inviting, with a soft and nurturing energy that also radiates vibrancy and vitality.

Design & Aesthetic:

I'd love to focus on rich rose gold tones
It should feel soft and approachable yet energetic and lively.

Functional Needs:

The site will support both my coaching services
and product sales, so it’s essential to have an intuitive and user-friendly shopping experience.
I'd love some exciting interactive features that keep visitors engaged and make the journey through the site feel seamless and uplifting.

Please let me know if there’s any additional information you need from me to bring this vision to life!

Thank you for your attention to these details! Here are some ideas I like to see Layout Ideas

Hero Section: An inviting header with a subtle half-moon background for a touch of healing energy.

Navigation & Logo: Place my logo in gold on the top left and use simple navigation links with a rose gold hover effect.

Section Dividers: Use small celestial icons, like a crescent moon, as dividers to create flow and add a bit of magic.

Product & Service Section: A soft rose gold gradient background to highlight products, with circular or wave accents around images.

Footer: Deep rose gold background with a half-moon icon to end with a warm invitation to connect.

Uploading an AI-generated image (it is a bit over the top but it captures the feel I like), with a hint of spirituality and femininity, along with elements like the half moon and colors. :) I'm also uploading my logos, and I have each option available in both color schemes.

Best,
Mirela

Industry/Entity Type

Health, Wellness

Coding

Coded - Design and coding required

Number of Pages Required

5+ page

Font styles to use
Other font styles liked:
• Playfair Display (Headings) & Lora (Body Text)

Requirements
Must have
• Shopify

```html
<!DOCTYPE html>
<html lang="en">
<head>
<meta charset="utf-8">
<title>VRB – Mirela Dovanski Wellness</title>
<link href="https://fonts.googleapis.com/css2?family=Playfair+Display:wght@400;700;800&family=Lora:wght@400;600&family=Arimo:wght@400&display=swap" rel="stylesheet">
<style>
:root{
  --rose:#bd5c4d;
  --rose-text:#bc5a4a;
  --blush:#f9b8a9;
  --ink:#111;
  --dark-frame:#2a1a18;
  --white:#fff;
  --black:#000;
  --moon-a:#e9a79d;
  --moon-b:#c9776a;
}
*{margin:0;padding:0;box-sizing:border-box}
html,body{width:1200px;height:1200px;overflow:hidden;background:var(--white)}
body{position:relative;font-family:"Lora",serif;color:var(--ink)}
.page{position:absolute;left:384px;top:0;width:433px;height:1200px}
.abs{position:absolute}
.center{left:0;right:0;text-align:center}
.display{font-family:"Playfair Display",serif;font-weight:700}

/* header */
.site-header{position:absolute;left:0;top:0;width:433px;height:40px;background:var(--white)}
.brand{left:29px;top:6px;display:flex;align-items:center;gap:4px;font-family:"Playfair Display",serif;font-size:12px;color:var(--rose-text)}
.brand-ring{width:22px;height:22px;border:1px solid var(--rose-text);border-radius:50%}
.main-nav{left:205px;top:15px;display:flex;gap:5px;font-family:"Playfair Display",serif;font-size:7px}
.main-nav .active{color:var(--rose-text);border-bottom:1px solid var(--rose-text);padding-bottom:2px}
.social{left:361px;top:13px;display:flex;gap:3px}
.social span{width:12px;height:12px;border:1px solid var(--rose-text);border-radius:50%}

/* hero */
.hero{position:absolute;left:0;top:40px;width:433px;height:210px;background:var(--rose)}
.hero-moon{left:252px;top:13px;width:61px;height:61px;border-radius:50%;background:radial-gradient(circle at 40% 35%,var(--moon-a),var(--moon-b))}
.hero-title{top:81px;font-size:21.5px;line-height:25.5px;color:var(--ink)}
.hero-sub{top:162px;font-size:5.5px}
.btn{display:inline-block;border:1px solid var(--white);border-radius:10px;color:var(--white);font-family:"Lora",serif;font-weight:600;font-size:6.3px;letter-spacing:.1px}
.hero .btn{position:absolute;left:169px;top:178px;width:96px;height:16px;line-height:14px;text-align:center}

/* disciplines */
.intro-title{top:280px;font-size:22px;line-height:25px;color:var(--rose-text)}
.intro-text{top:333px;font-size:5.5px;line-height:8.7px}
.divider{width:78px;height:10px;border-bottom:1px solid var(--ink);opacity:.8}
.divider-intro{left:178px;top:360px}
.discipline{width:120px;text-align:center;color:var(--rose-text);font-size:11px;line-height:14px}
.discipline i{display:block;width:24px;height:24px;border-radius:50%;background:var(--rose-text);margin:0 auto 8px}

/* services */
.services{position:absolute;left:0;top:594px;width:433px;height:299px;background:linear-gradient(var(--rose) 0%,#d67f6f 45%,var(--blush) 100%)}
.services-title{top:17px;font-size:22px;color:var(--ink)}
.services-text{top:47px;font-size:5.6px;line-height:8.7px;padding:0 60px}
.divider-services{left:177px;top:70px}
.card{position:absolute;top:96px;height:173px;border:2px solid var(--dark-frame);border-top:none;text-align:center;font-family:"Arimo",sans-serif}
.card.featured{background:var(--white);border-top:2px solid var(--dark-frame)}
.card-photo{position:absolute;left:10px;width:124px}
.card h3{position:absolute;left:0;right:0;font-family:"Playfair Display",serif;font-weight:700;font-size:10px}
.card p{position:absolute;left:10px;right:10px;font-size:5px;line-height:7.8px}

/* footer */
.site-footer{position:absolute;left:0;top:893px;width:433px;height:307px;background:var(--black);color:var(--white)}
.cta-title{top:16px;font-size:17px;line-height:19.5px;color:var(--rose-text)}
.cta-text{top:76px;font-size:6.5px;line-height:9.8px}
.site-footer .btn{position:absolute;left:169px;top:102px;width:96px;height:16px;line-height:14px;text-align:center}
.footer-nav{top:147px;display:flex;justify-content:center;gap:7px;font-family:"Playfair Display",serif;font-weight:700;font-size:6.3px}
.footer-nav span{text-decoration:underline}
.footer-brand{left:197px;top:175px;width:38px;height:38px;border:1px solid var(--rose-text);border-radius:50%;line-height:36px;text-align:center;font-family:"Playfair Display",serif;font-size:11px;color:var(--rose-text)}
.footer-name{top:215px;font-family:"Playfair Display",serif;font-size:7.5px;letter-spacing:.5px;color:var(--rose-text);text-transform:uppercase}
.contact{top:236px;font-weight:600;font-size:7px;line-height:10px}
.footer-rule{left:27px;width:379px;top:268px;border-top:1px solid #777}
.copyright{top:280px;font-family:"Arimo",sans-serif;font-size:5px}
</style>
</head>
<body>
<div class="page">

  <header class="site-header">
    <div class="abs brand"><span class="brand-ring"></span>VRB</div>
    <nav class="abs main-nav"><span class="active">Home</span><span>Programs</span><span>Labs</span><span>About</span><span>Testimonials</span></nav>
    <div class="abs social"><span></span><span></span><span></span></div>
  </header>

  <section class="hero">
    <div class="abs hero-moon" role="img" aria-label="Textured full moon illustration"></div>
    <h1 class="abs center display hero-title">Achieve Peak Health,<br>Productivity and Energy<br>with zero Stress</h1>
    <p class="abs center hero-sub">Are You Ready To Feel The Best You Have Ever Felt?</p>
    <a class="btn">BOOK A FREE CONSULT</a>
  </section>

  <section class="disciplines">
    <h2 class="abs center display intro-title">What is Integrative<br>Health?</h2>
    <p class="abs center intro-text">Integrative health coaching brings together<br>7 Different Integrated Disciplines</p>
    <div class="abs divider divider-intro" role="img" aria-label="Crescent moon and arrow divider ornament"></div>

    <div class="abs discipline display" style="left:29px;top:390px"><i role="img" aria-label="Mortar and herbs icon"></i>Ayurvedic Medicine</div>
    <div class="abs discipline display" style="left:158px;top:390px"><i role="img" aria-label="DNA icon"></i>Bioregulatory<br>Medicine</div>
    <div class="abs discipline display" style="left:286px;top:390px"><i role="img" aria-label="Herbal tea icon"></i>Medicine &amp;<br>Herbalism</div>
    <div class="abs discipline display" style="left:29px;top:456px"><i role="img" aria-label="Brain icon"></i>Eastern Philosopy</div>
    <div class="abs discipline display" style="left:158px;top:456px"><i role="img" aria-label="Leaf and hand icon"></i>Traditional<br>Naturophaty</div>
    <div class="abs discipline display" style="left:286px;top:456px"><i role="img" aria-label="Cells icon"></i>Orthomolecular<br>Medicine</div>
    <div class="abs discipline display" style="left:29px;top:524px"><i role="img" aria-label="Supplement bottle icon"></i>Functional Medicine</div>
  </section>

  <section class="services">
    <h2 class="abs center display services-title">Product &amp; Service</h2>
    <p class="abs center services-text">Curae hendrerit donec commodo hendrerit egestas tempus, turpis facilisis nostra nunc. Vestibulum dui eget ultrices.</p>
    <div class="abs divider divider-services" role="img" aria-label="Crescent moon and arrow divider ornament"></div>

    <article class="card" style="left:0;width:146px">
      <div class="card-photo" role="img" aria-label="Woman on a video call at a laptop" style="top:10px;height:75px;background:linear-gradient(135deg,#3d4a3a,#c9b9a5 60%,#6a4a34)"></div>
      <h3 style="top:88px">Zoom Consult</h3>
      <p style="top:103px">Lorem ipsum dolor sit amet, consectetur adipiscing elit, sed do eiusmod tempor incididunt ut labore et dolore magna aliqua. Ut enim ad minim veniam, quis nostrud exercitation ullamco laboris nisi ut aliquip ex ea commodo consequat.</p>
    </article>

    <article class="card featured" style="left:146px;width:144px">
      <div class="card-photo" role="img" aria-label="Scientist using a microscope in a lab" style="top:10px;height:82px;background:linear-gradient(135deg,#dfe5ee,#8a9bb5 50%,#2b4fa0)"></div>
      <h3 style="top:98px">Lab Testing</h3>
      <p style="top:112px">Lorem ipsum dolor sit amet, consectetur adipiscing elit, sed do eiusmod tempor incididunt ut labore et dolore magna aliqua. Ut enim ad minim veniam, quis nostrud exercitation ullamco laboris nisi ut aliquip ex ea commodo consequat.</p>
    </article>

    <article class="card" style="left:290px;width:143px">
      <div class="card-photo" role="img" aria-label="Family sharing a meal at home" style="top:10px;height:82px;background:linear-gradient(135deg,#4b3a2a,#a47a4e 50%,#2a2420)"></div>
      <h3 style="top:94px">Lifestyle Support</h3>
      <p style="top:109px">Lorem ipsum dolor sit amet, consectetur adipiscing elit, sed do eiusmod tempor incididunt ut labore et dolore magna aliqua. Ut enim ad minim veniam, quis nostrud exercitation ullamco laboris nisi ut aliquip ex ea commodo consequat.</p>
    </article>
  </section>

  <footer class="site-footer">
    <h2 class="abs center display cta-title">Are You Ready To Feel<br>The Best You Have Ever<br>Felt?</h2>
    <p class="abs center cta-text">Curae hendrerit donec commodo hendrerit egestas tempus,<br>turpis facilisis nostra nunc. Vestibulum dui eget ultrices.</p>
    <a class="btn">BOOK A FREE CONSULT</a>
    <nav class="abs center footer-nav"><span>HOME</span><span>PROGRAMS</span><span>LABS</span><span>ABOUT</span><span>TESTIMONIALS</span></nav>
    <div class="abs footer-brand">VRB</div>
    <p class="abs center footer-name">Mirela Dovanski Wellness</p>
    <div class="abs center contact">
      <p>Address Here, ...</p>
      <p><svg width="6" height="6" viewBox="0 0 24 24" style="vertical-align:-1px"><path fill="#fff" d="M6.6 10.8a15.1 15.1 0 0 0 6.6 6.6l2.2-2.2c.3-.3.7-.4 1-.2 1.1.4 2.3.6 3.6.6.6 0 1 .4 1 1V20c0 .6-.4 1-1 1A17 17 0 0 1 3 4c0-.6.4-1 1-1h3.5c.6 0 1 .4 1 1 0 1.3.2 2.5.6 3.6.1.3 0 .7-.2 1z"/></svg>(Phone Number)</p>
    </div>
    <div class="abs footer-rule"></div>
    <p class="abs center copyright">Copyright © 2024 VRB Mirela Dovanski Wellness</p>
  </footer>

</div>
</body>
</html>
```